Butcher shop

We have 2 butcher shops:

Shop 7, Ridgeway Court, Aberdeen NSW 2336
Ph 02 6519 4482

58 Partridge St, Scone NSW 2337
Ph 02 6538 2170

ABN 47 308 915 226

I would like this info on reverse of card and my personal info on front of card. I have a logo I would like to use also. Require a very smooth thick matte card, with colour both sides.

Front of card should say:

Lorna Tewsbury
Accounts

Ph 0427 615 903
E lornatewsbury@mailnest.example

Industry/Entity Type

Shop

Contact Information for Business Card

Lorna Tewsbury
Ph 0427 615 903

Logo Text

Tewsbury's Quality Meats

Logo styles of interest
Pictorial/Combination Logo
Requirements
Must have
• We use Century Gothic Font

```html
<!DOCTYPE html>
<html lang="en">
<head>
<meta charset="utf-8">
<title>Tewsbury's Quality Meats – Business Card</title>
<link rel="stylesheet" href="https://fonts.googleapis.com/css2?family=Didact+Gothic&family=Montserrat:wght@700&display=swap">
<style>
  :root {
    --sky: #87d3f1;
    --paper: #ffffff;
    --ink: #111111;
    --ink-soft: #1a1a1a;
  }
  html, body {
    margin: 0;
    padding: 0;
    overflow: hidden;
    background: var(--paper);
  }
  .card {
    position: relative;
    width: 1200px;
    height: 692px;
    overflow: hidden;
    background: var(--paper);
    font-family: "Didact Gothic", "Century Gothic", sans-serif;
    color: var(--ink);
  }
  .brand-panel {
    position: absolute;
    left: 0;
    top: 0;
    width: 599px;
    height: 692px;
    background: var(--sky);
  }
  .brand-name {
    position: absolute;
    left: 0;
    width: 599px;
    top: 196px;
    margin: 0;
    text-align: center;
    font-family: "Didact Gothic", "Century Gothic", sans-serif;
    font-weight: 400;
    font-size: 51px;
    line-height: 62px;
    color: var(--ink-soft);
  }
  .contact {
    position: absolute;
    left: 0;
    width: 599px;
    margin: 0;
    padding: 0;
    list-style: none;
  }
  .contact-item {
    position: absolute;
    left: 0;
    width: 599px;
    display: flex;
    justify-content: center;
    align-items: center;
    gap: 12px;
    white-space: nowrap;
  }
  .contact-phone {
    top: 550px;
    font-size: 37px;
  }
  .contact-email {
    top: 610px;
    font-size: 30px;
  }
  .contact-icon {
    flex: none;
  }
  .person {
    position: absolute;
    left: 599px;
    width: 601px;
    top: 296px;
    text-align: center;
  }
  .person-name {
    margin: 0;
    font-family: "Montserrat", "Century Gothic", sans-serif;
    font-weight: 700;
    font-size: 52px;
    line-height: 64px;
    letter-spacing: 0.5px;
  }
  .person-role {
    margin: 2px 0 0;
    font-size: 40px;
    line-height: 48px;
  }
</style>
</head>
<body>
  <main class="card">
    <section class="brand-panel">
      <h1 class="brand-name">Tewsbury's<br>Quality Meats</h1>
      <ul class="contact">
        <li class="contact-item contact-phone">
          <svg class="contact-icon" width="34" height="34" viewBox="0 0 34 34" aria-hidden="true">
            <circle cx="17" cy="17" r="15" fill="none" stroke="#111" stroke-width="2.5"/>
            <path d="M13 9 h4 l1 4 -2.5 1.5 c0 2 1 4 3 5.5 l2 -1.5 3 2.5 -1.5 3.5 c-5 0 -10 -6 -9 -15z" fill="#111"/>
          </svg>
          <span>0427 615 903</span>
        </li>
        <li class="contact-item contact-email">
          <svg class="contact-icon" width="42" height="30" viewBox="0 0 42 30" aria-hidden="true">
            <rect x="1.5" y="1.5" width="39" height="27" fill="none" stroke="#111" stroke-width="2"/>
            <path d="M1.5 1.5 L21 17 L40.5 1.5 M1.5 28.5 L16 13 M40.5 28.5 L26 13" fill="none" stroke="#111" stroke-width="2"/>
          </svg>
          <span>lornatewsbury@mailnest.example</span>
        </li>
      </ul>
    </section>
    <section class="person">
      <h2 class="person-name">Lorna Tewsbury</h2>
      <p class="person-role">Accounts</p>
    </section>
  </main>
</body>
</html>
```